Wine label design for my wife. Wine called "The Mirabel"

I need a wine label face lift of one of my premium wines in my collection. My wine sells in Harbor Lark's all over the States. My current label is called The Mirabel (my wife's name) and the illustration of her eyes is done by a well know artist from South Africa. I do not have to use this illustration and therefor I attached several pictures of her and her eyes, even when she was a little girl. The wine's also made in South Africa. This is a premium wine that we only sell 2000 bottles per year. The wine sells at 60 usd per bottle, The current label is too white. I also think her eyes should look more at the person buying it, than away from them.

Target Market(s)

Top end wine buyers

Font styles to use
Decorative
Script

Requirements
Must have
• 'The Mirabel' must be on the label
An illustration must be on the label
Basically all the info that's on the current label must be on by law. As per Sample
Nice to have
• Maybe some ideas of her whole face?
Should not have
• any gold colour

```html
<!DOCTYPE html>
<html lang="en">
<head>
<meta charset="utf-8">
<title>The Mirabel – Label Concepts</title>
<link rel="stylesheet" href="https://fonts.googleapis.com/css2?family=Great+Vibes&family=Pinyon+Script&family=Allura&family=Catamaran:wght@300;400;500&family=Tinos:wght@400;700&display=swap">
<style>
  :root {
    --ink: #000000;
    --paper: #ffffff;
    --wine: #990000;
    --accent-red: #e0141b;
    --band: #666666;
    --hairline: #999999;
  }
  html, body {
    margin: 0;
    padding: 0;
    width: 966px;
    height: 1200px;
    overflow: hidden;
    background: var(--paper);
  }
  .board { display: block; width: 966px; height: 1200px; }
  .band { fill: var(--band); }
  .label-black { fill: var(--ink); }
  .label-wine { fill: var(--wine); }
  .label-white { fill: var(--paper); stroke: var(--hairline); stroke-width: 1.5; }
  .rule-white { fill: none; stroke: var(--paper); stroke-width: 2.5; }
  .rule-black { fill: none; stroke: var(--ink); stroke-width: 1.5; }
  .rule-red { fill: none; stroke: var(--accent-red); stroke-width: 2.5; }

  .title { text-anchor: middle; }
  .title-vibes { font-family: "Great Vibes", cursive; }
  .title-pinyon { font-family: "Pinyon Script", cursive; }
  .title-allura { font-family: "Allura", cursive; }

  .varietal, .winery, .vintage { text-anchor: middle; }
  .sans { font-family: "Catamaran", sans-serif; font-weight: 500; }
  .sans-light { font-family: "Catamaran", sans-serif; font-weight: 300; letter-spacing: 3px; }
  .serif { font-family: "Tinos", serif; font-weight: 400; letter-spacing: 4px; }
  .serif-bold { font-family: "Tinos", serif; font-weight: 700; }

  .on-dark { fill: var(--paper); }
  .on-light { fill: var(--ink); }
</style>
</head>
<body>
<svg class="board" viewBox="0 0 1732 2150" preserveAspectRatio="none" xmlns="http://www.w3.org/2000/svg">
  <defs>
    <radialGradient id="portrait-mono" cx="50%" cy="50%" r="50%">
      <stop offset="0%" stop-color="#f4f4f4"/>
      <stop offset="70%" stop-color="#cfcfcf"/>
      <stop offset="100%" stop-color="#4a4a4a"/>
    </radialGradient>
    <radialGradient id="portrait-light" cx="50%" cy="50%" r="50%">
      <stop offset="0%" stop-color="#f2f2f2"/>
      <stop offset="75%" stop-color="#d4d4d4"/>
      <stop offset="100%" stop-color="#ffffff"/>
    </radialGradient>
    <radialGradient id="portrait-wine" cx="50%" cy="50%" r="50%">
      <stop offset="0%" stop-color="#eeeeee"/>
      <stop offset="70%" stop-color="#f8f0f0"/>
      <stop offset="100%" stop-color="#990000"/>
    </radialGradient>
  </defs>

  <rect class="band" x="0" y="655" width="1732" height="800"/>

  <!-- Concept 1: black square, framed -->
  <g class="concept concept-black-framed">
    <rect class="label-black" x="120" y="48" width="698" height="680" rx="55"/>
    <rect class="rule-white" x="137" y="67" width="663" height="644" rx="40"/>
    <text class="title title-vibes on-dark" x="468" y="198" font-size="118">The Mirabel</text>
    <text class="varietal sans on-dark" x="468" y="282" font-size="40">SAUVIIGNON BLANC 2017</text>
    <ellipse class="rule-white" cx="468" cy="458" rx="252" ry="135" stroke-width="1.5"/>
    <ellipse cx="468" cy="458" rx="234" ry="118" fill="url(#portrait-mono)" role="img" aria-label="Black and white portrait of the woman's eyes"/>
    <text class="winery sans on-dark" x="468" y="666" font-size="29">DANIEL FRAYNE WINES</text>
  </g>

  <!-- Concept 2: black square, fine script -->
  <g class="concept concept-black-fine">
    <rect class="label-black" x="930" y="48" width="700" height="680" rx="60"/>
    <text class="title title-allura on-dark" x="1280" y="222" font-size="150">The Mirabel</text>
    <text class="varietal sans-light on-dark" x="1280" y="304" font-size="40" letter-spacing="1">SAUVIIGNON BLANC 2017</text>
    <ellipse class="rule-white" cx="1280" cy="475" rx="252" ry="135" stroke-width="1.5"/>
    <ellipse cx="1280" cy="475" rx="234" ry="118" fill="url(#portrait-mono)" role="img" aria-label="Black and white portrait of the woman's eyes"/>
    <text class="winery sans-light on-dark" x="1280" y="667" font-size="29">DANIEL FRAYNE WINES</text>
  </g>

  <!-- Concept 3: white bracket -->
  <g class="concept concept-white-bracket">
    <path class="label-white" d="M140,770 C260,770 340,740 395,735 L440,735 Q462,738 470,752 Q478,738 500,735 L545,735 C600,740 680,770 805,770 Q822,770 822,788 L822,1355 Q822,1372 805,1372 C680,1372 600,1400 545,1407 L500,1407 Q478,1404 470,1390 Q462,1404 440,1407 L395,1407 C340,1400 260,1372 140,1372 Q122,1372 122,1355 L122,788 Q122,770 140,770 Z"/>
    <text class="title title-pinyon on-light" x="462" y="940" font-size="140">The Mirabel</text>
    <text class="varietal serif on-light" x="462" y="1006" font-size="40">SAUVIGNON BLANC 2017</text>
    <ellipse class="rule-black" cx="462" cy="1160" rx="228" ry="118"/>
    <ellipse cx="470" cy="1155" rx="215" ry="108" fill="url(#portrait-light)" role="img" aria-label="Black and white portrait of the woman's eyes"/>
    <text class="winery serif-bold on-light" x="462" y="1337" font-size="29">DANIEL FRAYNE WINES</text>
  </g>

  <!-- Concept 4: wine red ornate -->
  <g class="concept concept-wine-ornate">
    <path class="label-wine" d="M930,895 Q1000,880 1030,830 C1110,770 1190,740 1280,740 C1370,740 1450,770 1530,830 Q1560,880 1630,895 L1630,1250 Q1560,1262 1530,1310 C1450,1375 1370,1410 1280,1410 C1190,1410 1110,1375 1030,1310 Q1000,1262 930,1250 Z"/>
    <path class="rule-white" d="M948,910 Q1020,895 1045,848 C1120,790 1195,760 1280,760 C1365,760 1440,790 1515,848 Q1540,895 1612,910 L1612,1235 Q1540,1250 1515,1295 C1440,1360 1365,1392 1280,1392 C1195,1392 1120,1360 1045,1295 Q1020,1250 948,1235 Z"/>
    <text class="title title-vibes on-dark" x="1280" y="932" font-size="120">The Mirabel</text>
    <text class="varietal serif on-dark" x="1280" y="995" font-size="40" letter-spacing="2">SAUVIGNON BLANC</text>
    <ellipse class="rule-white" cx="1280" cy="1140" rx="228" ry="118" stroke-width="1.5"/>
    <ellipse cx="1280" cy="1140" rx="212" ry="104" fill="url(#portrait-wine)" role="img" aria-label="Black and white portrait of the woman's eyes"/>
    <text class="winery serif-bold on-dark" x="1280" y="1311" font-size="27">DANIEL FRAYNE WINES</text>
    <text class="vintage serif-bold on-dark" x="1280" y="1359" font-size="31">2017</text>
  </g>

  <!-- Concept 5: wine red square -->
  <g class="concept concept-wine-square">
    <rect class="label-wine" x="133" y="1415" width="700" height="680" rx="55"/>
    <text class="title title-pinyon on-dark" x="490" y="1580" font-size="128">The Mirabel</text>
    <text class="varietal serif on-dark" x="484" y="1646" font-size="42">SAUVIGNON BLANC 2017</text>
    <ellipse class="rule-white" cx="484" cy="1835" rx="252" ry="135" stroke-width="1.5"/>
    <ellipse cx="484" cy="1835" rx="236" ry="118" fill="url(#portrait-wine)" role="img" aria-label="Black and white portrait of the woman's eyes"/>
    <text class="winery serif on-dark" x="484" y="2042" font-size="34" letter-spacing="1">DANIEL FRAYNE WINES</text>
  </g>

  <!-- Concept 6: black stepped ornate -->
  <g class="concept concept-black-stepped">
    <path id="stepped-outline" class="label-black" d="M905,1745 C905,1650 940,1600 975,1590 L975,1560 L1080,1560 L1080,1525 L1135,1525 L1135,1500 Q1200,1425 1280,1425 Q1360,1425 1425,1500 L1425,1525 L1480,1525 L1480,1560 L1585,1560 L1585,1590 C1620,1600 1652,1650 1652,1745 C1652,1840 1620,1890 1585,1900 L1585,1930 L1480,1930 L1480,1965 L1425,1965 L1425,1990 Q1360,2090 1280,2090 Q1200,2090 1135,1990 L1135,1965 L1080,1965 L1080,1930 L975,1930 L975,1900 C940,1890 905,1840 905,1745 Z"/>
    <path class="rule-red" vector-effect="non-scaling-stroke" transform="translate(1278,1757) scale(0.955,0.94) translate(-1278,-1757)" d="M905,1745 C905,1650 940,1600 975,1590 L975,1560 L1080,1560 L1080,1525 L1135,1525 L1135,1500 Q1200,1425 1280,1425 Q1360,1425 1425,1500 L1425,1525 L1480,1525 L1480,1560 L1585,1560 L1585,1590 C1620,1600 1652,1650 1652,1745 C1652,1840 1620,1890 1585,1900 L1585,1930 L1480,1930 L1480,1965 L1425,1965 L1425,1990 Q1360,2090 1280,2090 Q1200,2090 1135,1990 L1135,1965 L1080,1965 L1080,1930 L975,1930 L975,1900 C940,1890 905,1840 905,1745 Z"/>
    <text class="title title-vibes on-dark" x="1278" y="1620" font-size="118">The Mirabel</text>
    <text class="varietal serif on-dark" x="1278" y="1684" font-size="34" letter-spacing="1.5">SAUVIGNON BLANC 2017</text>
    <ellipse class="rule-red" cx="1278" cy="1810" rx="205" ry="108" stroke-width="2"/>
    <ellipse cx="1275" cy="1808" rx="190" ry="96" fill="url(#portrait-mono)" role="img" aria-label="Black and white portrait of the woman's eyes"/>
    <text class="winery serif-bold on-dark" x="1280" y="1954" font-size="22" letter-spacing="1">DANIEL FRAYNE WINES</text>
  </g>
</svg>
</body>
</html>
```